Social Security Seminar

We need a creative postcard designed as an invitation, 5 X 7, full color, both sides.

These postcards will be used to invite prospects to attend a seminar series on social security planning.

We are a wealth management firm working with small business owners and families. Our average client is age 50-70 years old. We would like the postcard to be eye catching, but the design should reflect our conservative nature and appeal to an affluent clientele.

Our logo should be included on both sides of the card and the front of the postcard. The logo on the front can be more prominent.

On the back of the card, we do need to leave a section for the address, as well as ample blank space to add time and location of future seminars.

Our text has been reviewed and approved by our compliance and legal team and needs to be used as is. The disclosure statement that starts with "securities offered through...." should be on the back of the card at the bottom in a font no smaller than the smallest font on the card. It should be visible but not prominent.

The Twitter, Facebook and YouTube thumbnails should be included on the card to show that we are active on social media. Information about links to those social media pages is not needed on the card.

Pictures are provided for use in designing the card and may all be used but you don't have to use them all. The only picture that is mandatory is the picture of the 3 partners, placed on the back of the card.

The following questions are the points of interest for attendees and should be creatively and prominently displayed on the front of the postcard:
"When should I start taking my social security benefits?"
" What are my benefit payout options?"
"How will my social security benefit options affect my spouse?"
How comfortable are you with your social security plan?"

Similarly, the following are the points to be made on the back of the postcard:
"Join us for a free look into your social security benefit options."
"Seating is limited, so please RSVP either by email info@marlowcrestcapital.example or by phone 252-718-4032"
"Securities and advisory services offered through QRT Brokerage, a registered investment advisor. Member NEXA/DOVR"

Target Market(s)

Age 55 to 65, both male and female

Industry/Entity Type

Financial Planning

Font styles to use
Sans Serif

Colors
0555a3
e8e8e8

Requirements
Must have
• Clean modern look, design that will appeal to affluent clientele.
Should not have
• Do not deviate from text/verbage provided, which has be pre-approved from our compliance center

```html
<!DOCTYPE html>
<html lang="en">
<head>
<meta charset="utf-8">
<title>Marlowcrest Capital – Social Security Seminar Postcard</title>
<link href="https://fonts.googleapis.com/css2?family=Fira+Sans:wght@400;500;600&family=Roboto+Condensed:wght@400&display=swap" rel="stylesheet">
<style>
  :root {
    --brand-blue: #1b2a8f;
    --navy: #1f2f5c;
    --accent-blue: #0555a3;
    --panel-violet: rgba(98, 96, 186, 0.86);
    --band-grey: #c4c5c8;
    --soft-grey: #e8e8e8;
    --blank-grey: #f2f2f2;
    --ink: #222;
    --muted: #555;
    --rule: #c9c9c9;
    --page: #ececec;
    --white: #fff;
    --black: #0b0b0b;
  }
  * { box-sizing: border-box; margin: 0; padding: 0; }
  html, body { width: 889px; height: 1200px; overflow: hidden; }
  body { background: var(--page); font-family: "Fira Sans", sans-serif; color: var(--ink); position: relative; }

  .card { position: absolute; background: var(--white); overflow: hidden; box-shadow: 0 2px 6px rgba(0,0,0,.18); }
  .card--front { left: 75px; top: 67px; width: 658px; height: 470px; }
  .card--back { left: 142px; top: 636px; width: 659px; height: 469px; }

  /* Front */
  .front-photo { position: absolute; left: 0; top: 0; width: 658px; height: 413px;
    background: linear-gradient(135deg, #d9d4c6 0%, #cfcab9 35%, #bfc0c8 70%, #d4d0c2 100%); }
  .brand-tab { position: absolute; left: 27px; top: 0; width: 145px; height: 138px; background: var(--white);
    border-radius: 0 0 8px 8px; box-shadow: 0 2px 6px rgba(0,0,0,.25);
    display: flex; flex-direction: column; align-items: center; justify-content: center; gap: 4px; }
  .brand-name { font-family: "Fira Sans", sans-serif; font-weight: 500; color: var(--navy); text-align: center; line-height: 1.15; letter-spacing: 1.5px; }
  .brand-tab .brand-name { font-size: 15px; }
  .brand-mark { width: 14px; height: 14px; background: var(--navy); }

  .question-panel { position: absolute; left: 196px; top: 89px; width: 437px; height: 258px; background: var(--panel-violet);
    padding: 26px 24px 0 34px; }
  .question-list { list-style: none; }
  .question-list li { position: relative; color: var(--white); font-size: 20.5px; line-height: 25px; margin-bottom: 12px; padding-left: 18px; }
  .question-list li::before { content: "»"; position: absolute; left: 0; top: -1px; }

  .front-footer { position: absolute; left: 0; bottom: 0; width: 100%; height: 57px; background: var(--band-grey);
    border-top: 2px solid var(--brand-blue); display: flex; align-items: center; justify-content: space-between; padding: 0 22px; }
  .web-address { font-size: 19px; color: #2a2a2a; }
  .social-row { display: flex; gap: 9px; }
  .social-chip { background: var(--black); }
  .front-footer .social-chip { width: 31px; height: 31px; }

  /* Back */
  .back-header { position: absolute; left: 0; top: 0; width: 334px; height: 101px; }
  .back-header .brand-block { position: absolute; left: 14px; top: 22px; width: 120px; display: flex; flex-direction: column; align-items: center; gap: 4px; }
  .back-header .brand-name { font-size: 13px; }
  .invite-headline { position: absolute; left: 154px; top: 36px; width: 180px; font-size: 13px; line-height: 16px; color: var(--brand-blue); text-transform: uppercase; }

  .event-details { position: absolute; left: 0; top: 101px; width: 334px; height: 107px; background: var(--blank-grey); }
  .partners-photo { position: absolute; left: 0; top: 208px; width: 334px; height: 162px;
    background: linear-gradient(180deg, #8e9a78 0%, #6f7d5a 45%, #3b4150 75%, #8b7a62 100%); }
  .rsvp-bar { position: absolute; left: 0; top: 372px; width: 336px; height: 33px; background: var(--black);
    color: var(--white); font-weight: 600; font-size: 12px; padding: 9px 0 0 18px; }
  .rsvp-details { position: absolute; left: 0; top: 405px; width: 336px; height: 64px; background: var(--band-grey); padding: 9px 0 0 18px; }
  .rsvp-details p { font-size: 11px; line-height: 15.5px; color: #222; white-space: nowrap; }
  .rsvp-details .social-row { position: absolute; right: 12px; top: 25px; gap: 5px; }
  .rsvp-details .social-chip { width: 15px; height: 15px; }

  .return-address { position: absolute; left: 368px; top: 42px; font-family: "Roboto Condensed", sans-serif; font-style: normal; font-size: 9.5px; line-height: 14px; color: var(--muted); }
  .stamp-box { position: absolute; left: 541px; top: 32px; width: 89px; height: 72px; border: 1px solid #bdbdbd; }
  .address-lines { position: absolute; left: 432px; top: 216px; width: 199px; }
  .address-lines span { display: block; height: 30px; border-top: 1px solid var(--rule); }
  .disclosure { position: absolute; left: 346px; top: 419px; width: 302px; text-align: center; font-size: 11px; line-height: 14px; color: var(--muted); white-space: nowrap; }
</style>
</head>
<body>

<section class="card card--front" aria-label="Postcard front">
  <div class="front-photo" role="img" aria-label="Close-up photo of banknotes and a social security card"></div>
  <div class="brand-tab">
    <span class="brand-mark"></span>
    <span class="brand-name">MARLOWCREST<br>CAPITAL</span>
  </div>
  <div class="question-panel">
    <ul class="question-list">
      <li>When should I start taking my social security benefits?</li>
      <li>What are my benefit payout options?</li>
      <li>How will my social security benefit options affect my spouse?</li>
      <li>How comfortable are you with your social security plan?</li>
    </ul>
  </div>
  <div class="front-footer">
    <span class="web-address">www.marlowcrestcapital.example</span>
    <div class="social-row" aria-label="Social media channels">
      <span class="social-chip" role="img" aria-label="Social channel"></span>
      <span class="social-chip" role="img" aria-label="Social channel"></span>
      <span class="social-chip" role="img" aria-label="Video channel"></span>
    </div>
  </div>
</section>

<section class="card card--back" aria-label="Postcard back">
  <header class="back-header">
    <div class="brand-block">
      <span class="brand-mark"></span>
      <span class="brand-name">MARLOWCREST<br>CAPITAL</span>
    </div>
    <p class="invite-headline">Join us for a free look into your social security benefit options.</p>
  </header>
  <div class="event-details" aria-label="Space for seminar time and location"></div>
  <div class="partners-photo" role="img" aria-label="Photo of the three firm partners in suits standing outdoors"></div>
  <div class="rsvp-bar">Seating is limited, so please RSVP:</div>
  <div class="rsvp-details">
    <p>- by email info@marlowcrestcapital.example</p>
    <p>- by phone 252-718-4032</p>
    <p>- visit our website www.marlowcrestcapital.example</p>
    <div class="social-row" aria-label="Social media channels">
      <span class="social-chip" role="img" aria-label="Social channel"></span>
      <span class="social-chip" role="img" aria-label="Social channel"></span>
      <span class="social-chip" role="img" aria-label="Video channel"></span>
    </div>
  </div>

  <address class="return-address">
    Marlowcrest Capital<br>
    418 W Harbor Ln, Ste C-2<br>
    Larkfield, NC 27999
  </address>
  <div class="stamp-box" aria-label="Stamp area"></div>
  <div class="address-lines" aria-label="Mailing address area">
    <span></span><span></span><span></span><span></span><span></span>
  </div>
  <p class="disclosure">Securities and advisory services offered through<br>QRT Brokerage, a registered investment advisor.<br>Member NEXA/DOVR</p>
</section>

</body>
</html>
```